Ember Relaywork - Field Service Brochure

We are looking for a one page marketing brochure that includes our rate sheet. I've attached the working we on on the rate page, several photos and several versions of our logo.

```html
<!DOCTYPE html>
<html lang="en">
<head>
<meta charset="utf-8">
<title>Ember Relaywork – Field Service Rate Sheet</title>
<link href="https://fonts.googleapis.com/css2?family=Arimo:wght@400;700&display=swap" rel="stylesheet">
<style>
  :root {
    --steel: #46729a;
    --steel-light: #5b86ad;
    --paper: #ffffff;
    --ink: #1e1e1e;
    --backdrop: #e9e6e1;
    --rule: rgba(255,255,255,0.45);
  }
  * { margin: 0; padding: 0; box-sizing: border-box; }
  html, body { width: 1200px; height: 800px; overflow: hidden; background: var(--backdrop); }
  body { font-family: "Arimo", Arial, sans-serif; color: var(--ink); }

  .flyer {
    position: absolute; left: 306px; top: 20px;
    width: 588px; height: 760px;
    background: var(--paper);
    overflow: hidden;
    box-shadow: 0 6px 22px rgba(0,0,0,0.18);
  }
  .flyer__header { position: absolute; left: 0; top: 0; width: 588px; height: 290px; }

  .brand {
    position: absolute; right: 30px; top: 200px;
    display: flex; align-items: center; gap: 9px;
    color: var(--steel); font-weight: 700; font-size: 24px; letter-spacing: 0.5px;
  }
  .brand__mark { width: 15px; height: 15px; background: var(--steel); }

  .flyer__body {
    position: absolute; left: 30px; right: 30px; top: 298px; bottom: 20px;
    display: flex; flex-direction: column;
  }

  .intro { font-size: 10.5px; line-height: 1.42; margin-bottom: 12px; }

  .rate-grid {
    display: grid; grid-template-columns: 1fr 1fr;
    column-gap: 22px; row-gap: 12px; align-items: start;
  }

  .rate-block__title { color: var(--steel); font-weight: 700; font-size: 16px; line-height: 1.2; }
  .rate-block__note { font-size: 9.5px; margin: 2px 0 4px; }

  .rate-table { background: var(--steel); color: #fff; padding: 3px 10px; font-size: 9.5px; }
  .rate-table__row { display: flex; gap: 10px; padding: 4px 0; border-bottom: 1px solid var(--rule); line-height: 1.3; }
  .rate-table__row:last-child { border-bottom: none; }
  .rate-table__key { flex: 0 0 60px; }
  .rate-table__key--wide { flex: 0 0 92px; }

  .rate-list { background: var(--steel); color: #fff; padding: 7px 10px 5px 22px; font-size: 9.5px; line-height: 1.3; margin-top: 4px; }
  .rate-list li { margin-bottom: 3px; }
  .rate-table--expenses { margin-top: 4px; }

  .contact-line { margin-top: auto; padding-bottom: 12px; text-align: center; font-size: 10.5px; }
  .flyer__footer-band { position: absolute; left: 0; right: 0; bottom: 0; height: 20px; background: var(--steel); }
</style>
</head>
<body>
<article class="flyer">
  <svg class="flyer__header" viewBox="0 0 588 290">
    <defs>
      <linearGradient id="fieldPhotoTone" x1="0" y1="0" x2="1" y2="1">
        <stop offset="0" stop-color="#3f6fc4"/>
        <stop offset="0.55" stop-color="#8a9aa8"/>
        <stop offset="1" stop-color="#b49a74"/>
      </linearGradient>
    </defs>
    <polygon points="0,0 588,0 588,100 0,262" fill="url(#fieldPhotoTone)" role="img"
             aria-label="Photo of field technicians in hard hats working on a lift beside high-voltage switchgear insulators, with utility trucks behind"/>
    <polygon points="0,262 588,100 588,110 0,272" fill="var(--steel-light)"/>
    <polygon points="0,274 588,112 588,122 0,284" fill="var(--steel)"/>
  </svg>

  <div class="brand"><span class="brand__mark"></span>Ember Relaywork</div>

  <div class="flyer__body">
    <p class="intro">Ember Relaywork Company offers an expertly trained Field Service program that can provide technical guidance and assistance for your initial installation, sustaining maintenance, and repair of equipment manufactured by Ember Relaywork. A 4-6 week reservation for assistance is recommended to ensure that we can fully accommodate your desired schedule. Expedited service may be available upon request.</p>

    <div class="rate-grid">
      <section class="rate-block">
        <h2 class="rate-block__title">Standard Rate</h2>
        <p class="rate-block__note">(on-site) up to 10 hours + travel and per diem expenses</p>
        <div class="rate-table">
          <div class="rate-table__row"><span class="rate-table__key">$250 x 1.00</span><span>Monday through Friday rate per hour ($2500 minimum)</span></div>
          <div class="rate-table__row"><span class="rate-table__key">$250 x 1.50</span><span>Saturday rate per hour</span></div>
          <div class="rate-table__row"><span class="rate-table__key">$250 X 2.00</span><span>Sunday rate per hour</span></div>
        </div>
      </section>

      <section class="rate-block">
        <h2 class="rate-block__title">Premium Rates</h2>
        <p class="rate-block__note">(on-site) over 8 hours +travel and per diem expenses</p>
        <div class="rate-table">
          <div class="rate-table__row"><span class="rate-table__key">$250 X 1.50</span><span>Over Time (8-12 hours) rate per hour</span></div>
          <div class="rate-table__row"><span class="rate-table__key">$250 x 2.00</span><span>Double Time (Over 12 hours) rate per hour</span></div>
          <div class="rate-table__row"><span class="rate-table__key">$250 X 2.50</span><span>Non-standard overnight hours</span></div>
        </div>
      </section>

      <section class="rate-block">
        <h2 class="rate-block__title">Expenses</h2>
        <div class="rate-table rate-table--expenses">
          <div class="rate-table__row"><span class="rate-table__key rate-table__key--wide">Airfare</span><span>invoiced at actual cost + 25%</span></div>
          <div class="rate-table__row"><span class="rate-table__key rate-table__key--wide">Lodging</span><span>invoiced at actual cost + 25%</span></div>
          <div class="rate-table__row"><span class="rate-table__key rate-table__key--wide">Meals and Incidentals</span><span>invoiced at cost (not to exceed $100/day)</span></div>
          <div class="rate-table__row"><span class="rate-table__key rate-table__key--wide">Rental Vehicle and related costs</span><span>invoiced at cost +25%</span></div>
        </div>
      </section>

      <section class="rate-block">
        <h2 class="rate-block__title">Minimum Charge</h2>
        <ul class="rate-list">
          <li>The minimum charge, excluding travel time and expenses shall be the equivalent of one 10 hour day</li>
          <li>Cancellation charge of 4 standard hours plus any non-cancellable airfare or lodging charges shall apply</li>
          <li>Employee Drug Screening</li>
          <li>Drug screening and/or background check costs (if required by customer) shall be invoiced at actual cost plus 30%.</li>
        </ul>
      </section>
    </div>

    <p class="contact-line">1470 Kestrel Road N.W. • Dunmore, AL 35410 • 205-555-0172 • 800-555-0138 • Fax: 205-555-0179</p>
  </div>

  <div class="flyer__footer-band"></div>
</article>
</body>
</html>
```